Create a landing page for my local business that I’m looking to advertise

I own an oriental rug repair, restoration and cleaning business.
I’m looking to rug advertising and i would like a very clear *******UX and UI design******* website designed.

pages that i need:
-Repair and restoration
-Cleaning
-Blocking
-Staircase rug installation
_about us
-homepage
-our story
-contact us
-estimate

Www.velorantex.com

Industry/Entity Type

Rug Industry, Antique and New Rug Repair restoration and cleaning

Number of Pages Required

5+ page

Font styles to use
Serif
Sans Serif
Script

Colors
6B429C
8869AF
B7A5CE
E3DAEB
F3F0F8

Requirements
Must have
• IT HAS TO PRESENT FINE RUG REPAIR, RESTORATION AND CLEANING.
Should not have
• I DONT WANT THE WEBSITE TO LOOK LIKE A GENERIC “CLEANING COMPANY”. WE ARE A HIGH END RUG REPAIR ,RESTORATION AND CLEANING COMPANY

```html
<!DOCTYPE html>
<html lang="en">
<head>
<meta charset="utf-8">
<title>Velorantex — Rug Repair, Restoration &amp; Cleaning</title>
<link rel="stylesheet" href="https://fonts.googleapis.com/css2?family=Urbanist:wght@400;500;600;700&display=swap">
<style>
:root{
  --plum:#6B429C;
  --violet:#8869AF;
  --lilac:#B7A5CE;
  --mist:#E3DAEB;
  --haze:#F3F0F8;
  --band:#8869AF;
  --band-edge:#6B429C;
  --ink:#1d1d1d;
  --text:#3a3a3a;
  --muted:#6b6b6b;
  --line:#d9d9d9;
  --footer:#1d1528;
  --white:#ffffff;
}
*{box-sizing:border-box;margin:0;padding:0}
html,body{width:1200px;height:2981px;overflow:hidden}
body{position:relative;background:var(--white);font-family:"Urbanist",sans-serif;color:var(--text)}
.abs{position:absolute}

/* header */
.site-header{position:absolute;left:0;top:0;width:1200px;height:100px;background:var(--white);z-index:3}
.brand{position:absolute;left:163px;top:36px;display:flex;align-items:center;gap:10px;font-weight:700;font-size:24px;color:var(--ink)}
.brand-dot{width:26px;height:26px;border-radius:50%;border:2px solid var(--plum)}
.main-nav{position:absolute;top:42px;left:0;width:1200px;font-size:16px;font-weight:500;color:var(--ink)}
.main-nav a{position:absolute;color:inherit;text-decoration:none}
.main-nav a.active{color:var(--plum);padding-bottom:6px;border-bottom:2px solid var(--plum)}
.nav-divider{position:absolute;left:893px;top:42px;width:1px;height:22px;background:var(--line)}
.phone-btn{position:absolute;left:923px;top:37px;width:157px;height:33px;border:2px solid var(--violet);border-radius:17px;display:flex;align-items:center;justify-content:center;gap:10px;font-size:15px;font-weight:500;color:var(--ink)}

/* hero */
.hero-photo{position:absolute;left:0;top:100px;width:1200px;height:610px;
  background:linear-gradient(90deg,rgba(255,255,255,.85) 0%,rgba(255,255,255,.35) 35%,rgba(255,255,255,0) 55%),
  radial-gradient(ellipse at 50% 60%,#3a2418 0%,#6b3b22 35%,#a86b3c 65%,#e8d2b0 100%)}
.hero-title{position:absolute;left:163px;top:262px;font-size:44px;line-height:60px;font-weight:700;color:#111}
.btn-solid{position:absolute;background:var(--plum);color:var(--white);font-weight:500;display:flex;align-items:center;justify-content:center}
.hero-btn{left:163px;top:400px;width:141px;height:39px;border-radius:20px;font-size:13px}

/* about */
.about-blob{position:absolute;left:-260px;top:800px;width:320px;height:340px;border-radius:50%;background:var(--haze)}
.about-rule{position:absolute;left:163px;top:862px;width:51px;height:3px;background:var(--violet)}
.about-copy{position:absolute;left:163px;top:882px;width:430px;font-size:15px;line-height:27.5px;color:var(--text);white-space:nowrap}
.btn-outline{position:absolute;left:163px;top:1095px;width:146px;height:40px;border:1.5px solid var(--violet);border-radius:20px;display:flex;align-items:center;justify-content:center;font-size:15px;font-weight:600;color:var(--ink)}
.about-photo{position:absolute;left:680px;top:769px;width:412px;height:412px;border-radius:50%;
  background:linear-gradient(160deg,#e9e2d8 0%,#d8cfc2 25%,#5a1f1f 45%,#2a1a16 70%,#6b2a22 100%)}
.exp-badge{position:absolute;left:614px;top:1016px;width:139px;height:51px;background:var(--plum);border-radius:4px;color:var(--white);display:flex;align-items:center;padding-left:14px;gap:10px}
.exp-badge b{font-size:20px;font-weight:600}
.exp-badge span{font-size:13.5px;line-height:16px}
.ring{position:absolute;border:2px solid var(--violet);border-radius:50%}

/* services */
.services-bg{position:absolute;left:0;top:1250px}
.services-title{position:absolute;left:0;top:1382px;width:1200px;text-align:center;font-size:47px;font-weight:600;color:var(--white)}
.services-sub{position:absolute;left:250px;top:1452px;width:700px;text-align:center;font-size:17px;line-height:27px;color:var(--white)}
.service-card{position:absolute;background:var(--white);border-radius:3px;text-align:center}
.service-card svg{position:absolute;left:50%;top:28px;transform:translateX(-50%)}
.service-card h3{position:absolute;left:0;width:100%;top:116px;font-size:17px;font-weight:600;color:var(--ink)}
.service-card p{position:absolute;left:0;width:100%;top:144px;font-size:11.5px;line-height:19.5px;color:var(--muted)}

/* contact */
.contact-title{position:absolute;left:0;top:2272px;width:1200px;text-align:center;font-size:33px;font-weight:700;color:var(--ink);letter-spacing:.5px}
.footer-bg{position:absolute;left:0;top:2500px}
.contact-card{position:absolute;left:193px;top:2346px;width:814px;height:301px;background:var(--white);border-top:3px solid var(--violet);box-shadow:0 2px 12px rgba(0,0,0,.06)}
.contact-card h4{position:absolute;left:90px;top:28px;font-size:19px;font-weight:500;color:var(--ink)}
.field{position:absolute;border:1px solid #cfcfcf;border-radius:2px;font-size:11px;color:#9a9a9a;padding:9px 15px}
.submit{left:283px;top:2586px;width:117px;height:30px;font-size:13px;font-weight:600}

/* footer */
.footer-brand{position:absolute;left:194px;top:2725px;width:81px;height:81px;background:var(--white);display:flex;align-items:center;justify-content:center;font-size:13px;font-weight:700;color:var(--ink)}
.footer-text{position:absolute;font-size:12px;color:#e8e8e8}
.footer-head{position:absolute;font-size:13px;font-weight:700;color:var(--white)}
.footer-rule{position:absolute;height:1px;background:#3e3350}
.newsletter-input{position:absolute;left:827px;top:2787px;width:108px;height:24px;background:var(--white)}
.newsletter-btn{position:absolute;left:935px;top:2787px;width:72px;height:24px;background:var(--violet);color:var(--white);font-size:11.5px;display:flex;align-items:center;justify-content:center}
.social{position:absolute;top:2834px;width:20px;height:20px;border:1px solid #e8e8e8;border-radius:50%}
</style>
</head>
<body>

<header class="site-header">
  <div class="brand"><span class="brand-dot"></span>Velorantex</div>
  <nav class="main-nav">
    <a class="active" style="left:513px">Home</a>
    <a style="left:590px">About Us</a>
    <a style="left:690px">Services</a>
    <a style="left:784px">Contact Us</a>
  </nav>
  <span class="nav-divider"></span>
  <div class="phone-btn">
    <svg width="14" height="14" viewBox="0 0 24 24"><path fill="#6B429C" d="M6.6 10.8a15 15 0 0 0 6.6 6.6l2.2-2.2c.3-.3.7-.4 1-.2 1.1.4 2.3.6 3.6.6.6 0 1 .4 1 1V20c0 .6-.4 1-1 1A17 17 0 0 1 3 4c0-.6.4-1 1-1h3.5c.6 0 1 .4 1 1 0 1.3.2 2.5.6 3.6.1.3 0 .7-.2 1z"/></svg>
    012 9876 543
  </div>
</header>

<section>
  <div class="hero-photo" role="img" aria-label="Photo of a patterned oriental runner installed on a curved staircase with wrought iron balusters"></div>
  <svg class="abs" style="left:0;top:620px" width="1200" height="100" viewBox="0 0 1200 100">
    <path d="M0 16 Q600 150 1200 16 L1200 100 L0 100Z" fill="#8869AF"/>
    <path d="M0 30 Q600 156 1200 30 L1200 100 L0 100Z" fill="#ffffff"/>
  </svg>
  <h1 class="hero-title">Lorem Ipsum is simply<br>dummy text</h1>
  <div class="btn-solid hero-btn">LEARN MORE</div>
</section>

<section>
  <div class="about-blob"></div>
  <span class="about-rule"></span>
  <p class="about-copy">We provide generally accepted good practices by offering a<br>wide-ranging consulting/pre &amp; post contracting planning/<br>scheduling roadmap service(s) for independent professionals,<br>organizations and projects that represents how and when so<br>that required actions can be implemented as necessary to<br>achieve the strategic goals as planned.</p>
  <div class="btn-outline">Learn More</div>
  <div class="about-photo" role="img" aria-label="Photo of a dark red oriental rug fitted on a stair landing"></div>
  <div class="exp-badge"><b>10+</b><span>Years<br>Experience</span></div>
  <span class="ring" style="left:1015px;top:1141px;width:42px;height:42px"></span>
  <span class="ring" style="left:1080px;top:1156px;width:25px;height:25px;border-width:1.5px;border-color:#B7A5CE"></span>
</section>

<section>
  <svg class="services-bg" width="1200" height="1000" viewBox="0 0 1200 1000">
    <path d="M0 121 Q600 -75 1200 121 L1200 873 Q600 1035 0 873Z" fill="#8869AF"/>
    <path d="M0 121 Q600 -75 1200 121" fill="none" stroke="#6B429C" stroke-width="6"/>
    <path d="M0 873 Q600 1035 1200 873" fill="none" stroke="#6B429C" stroke-width="6"/>
  </svg>
  <h2 class="services-title">Services We Provide</h2>
  <p class="services-sub">Our business vision is to Plan, Track work to aim to Achieve success and results coordinating support for Industries, Individuals, Organizations that includes.</p>

  <article class="service-card" style="left:163px;top:1545px;width:272px;height:239px">
    <svg width="74" height="74" viewBox="0 0 74 74" fill="#6B429C"><rect x="33" y="2" width="5" height="70"/><rect x="4" y="12" width="20" height="11" rx="2"/><rect x="4" y="34" width="20" height="11" rx="2"/><rect x="46" y="22" width="22" height="11" rx="2"/><rect x="46" y="50" width="22" height="11" rx="2"/><rect x="24" y="16" width="9" height="3"/><rect x="24" y="38" width="9" height="3"/><rect x="38" y="26" width="8" height="3"/><rect x="38" y="54" width="8" height="3"/></svg>
    <h3>Repair and restoration</h3>
    <p>Lorem Ipsum is simply dummy text of the<br>and typesetting industry. Lorem<br>been the industry's standard</p>
  </article>
  <article class="service-card" style="left:464px;top:1545px;width:273px;height:239px">
    <svg width="74" height="74" viewBox="0 0 74 74" fill="#6B429C"><rect x="2" y="2" width="22" height="22"/><rect x="50" y="2" width="22" height="22"/><rect x="2" y="50" width="22" height="22"/><rect x="50" y="50" width="22" height="22"/><path d="M28 13h12l-4-4M44 61H32l4 4M13 28v12l-4-4M61 44V32l4 4" fill="none" stroke="#6B429C" stroke-width="4"/></svg>
    <h3>Cleaning</h3>
    <p>Lorem Ipsum is simply dummy text of the<br>and typesetting industry. Lorem<br>been the industry's standard</p>
  </article>
  <article class="service-card" style="left:765px;top:1545px;width:273px;height:239px">
    <svg width="74" height="74" viewBox="0 0 74 74" fill="#6B429C"><circle cx="12" cy="10" r="7"/><circle cx="62" cy="10" r="7"/><circle cx="12" cy="40" r="7"/><circle cx="62" cy="40" r="7"/><path d="M19 10h36M12 17v16M62 17v16" stroke="#6B429C" stroke-width="3"/><path d="M4 72q4-22 33-18q29-4 33 18z"/><circle cx="37" cy="50" r="7" fill="#fff"/></svg>
    <h3>Blocking</h3>
    <p>Lorem Ipsum is simply dummy text of the<br>and typesetting industry. Lorem<br>been the industry's standard</p>
  </article>
  <article class="service-card" style="left:251px;top:1813px;width:335px;height:240px">
    <svg width="74" height="74" viewBox="0 0 74 74" fill="#6B429C"><circle cx="37" cy="14" r="10"/><circle cx="37" cy="14" r="4" fill="#fff"/><circle cx="10" cy="22" r="6"/><circle cx="64" cy="22" r="6"/><path d="M4 32h12v36H4zM58 32h12v36H58zM22 38h30v8H40v22h-6V46H22z"/></svg>
    <h3>Staircase rug installation</h3>
    <p>Lorem Ipsum is simply dummy text of the<br>and typesetting industry. Lorem<br>been the industry's standard</p>
  </article>
  <article class="service-card" style="left:614px;top:1813px;width:335px;height:240px">
    <svg width="74" height="74" viewBox="0 0 74 74" fill="#6B429C"><circle cx="37" cy="10" r="9"/><circle cx="37" cy="62" r="9"/><circle cx="10" cy="36" r="9"/><circle cx="64" cy="36" r="9"/><path d="M6 36l3 3 5-6M60 36l3 3 5-6" stroke="#fff" stroke-width="2" fill="none"/><path d="M22 14l-6 8M52 14l6 8M22 58l-6-8M52 58l6-8" stroke="#6B429C" stroke-width="3"/></svg>
    <h3 style="top:114px">About us</h3>
    <p style="top:141px">Lorem Ipsum is simply dummy text of the<br>and typesetting industry. Lorem<br>been the industry's standard</p>
  </article>
</section>

<section>
  <h2 class="contact-title">CONTACT</h2>
  <svg class="footer-bg" width="1200" height="481" viewBox="0 0 1200 481">
    <path d="M0 34 Q600 150 1200 34 L1200 481 L0 481Z" fill="#1d1528"/>
  </svg>
  <form class="contact-card">
    <h4>Feel Free to Contact Us</h4>
  </form>
  <div class="field" style="left:283px;top:2410px;width:311px;height:30px">First Name</div>
  <div class="field" style="left:606px;top:2410px;width:311px;height:30px">Last Name</div>
  <div class="field" style="left:283px;top:2454px;width:311px;height:30px">Email</div>
  <div class="field" style="left:606px;top:2454px;width:311px;height:30px">Subject</div>
  <div class="field" style="left:283px;top:2498px;width:634px;height:74px">Message...</div>
  <div class="btn-solid submit">SUBMIT</div>
</section>

<footer>
  <div class="footer-brand">Velorantex</div>
  <svg class="abs" style="left:194px;top:2836px" width="15" height="13" viewBox="0 0 15 13"><rect x="1" y="3" width="13" height="9" fill="none" stroke="#e8e8e8"/><path d="M1 3l6.5 5 6.5-5" fill="none" stroke="#e8e8e8"/></svg>
  <span class="footer-text" style="left:225px;top:2836px">name@velorantex.com.</span>

  <span class="footer-head" style="left:511px;top:2727px">SITELINKS</span>
  <span class="footer-rule" style="left:511px;top:2751px;width:158px"></span>
  <span class="footer-text" style="left:511px;top:2763px">Home</span>
  <span class="footer-text" style="left:511px;top:2787px">About Us</span>
  <span class="footer-text" style="left:511px;top:2811px">Services</span>
  <span class="footer-text" style="left:511px;top:2835px">Sitemap</span>
  <span class="footer-text" style="left:511px;top:2859px">Contact</span>

  <span class="footer-head" style="left:827px;top:2727px">STAY IN TOUCH</span>
  <span class="footer-rule" style="left:827px;top:2751px;width:180px"></span>
  <span class="footer-text" style="left:827px;top:2763px">Subscribe Our Newsletter</span>
  <div class="newsletter-input"></div>
  <div class="newsletter-btn">Subscribe</div>
  <span class="social" style="left:827px"></span>
  <span class="social" style="left:852px"></span>
  <span class="social" style="left:876px"></span>

  <span class="footer-rule" style="left:194px;top:2911px;width:813px"></span>
  <span class="footer-text" style="left:246px;top:2930px;font-size:11.5px">@velorantex. All Rights Reserved.</span>
  <span class="footer-text" style="left:784px;top:2930px;font-size:11.5px">Privacy &amp; Policy &nbsp;| &nbsp;Faq &nbsp;| &nbsp;Terms.</span>
</footer>

</body>
</html>
```